Health care technology software systems

We have a solid logo. We have company colors that will need to be used as well. We just need a great business card design. We sell to health plans but want to be modern
Updates

Need extra days to review

Target Market(s)

Health technology sector selling into Health Plans

Industry/Entity Type

Health Care Technology

Contact Information for Business Card

Name, title, address, phone number, email

Requirements
Must have
• Use of Kembrata corporate colors - Uploaded w/ our logos

```html
<!DOCTYPE html>
<html lang="en">
<head>
<meta charset="utf-8">
<title>Kembrata Business Card</title>
<link href="https://fonts.googleapis.com/css2?family=Montserrat:wght@300;400;500;700&display=swap" rel="stylesheet">
<style>
  :root {
    --brand-green: #8cc63f;
    --brand-green-soft: #9bd053;
    --brand-blue: #29a8e0;
    --ink: #222222;
    --logo-ink: #3d3d3d;
    --paper: #ffffff;
    --backdrop: #e6e7e9;
  }
  * { box-sizing: border-box; margin: 0; padding: 0; }
  html, body {
    width: 1200px; height: 900px; overflow: hidden;
    background: var(--backdrop);
    font-family: "Montserrat", Arial, sans-serif;
  }
  .stage { position: relative; width: 1200px; height: 900px; }
  .card {
    position: absolute; left: 250px; width: 700px; height: 400px;
    overflow: hidden; box-shadow: 0 6px 18px rgba(0,0,0,0.18);
  }
  /* Front */
  .card-front { top: 40px; background: var(--brand-green); }
  .world-map-area {
    position: absolute; left: 70px; top: 60px; width: 560px; height: 280px;
    border-radius: 40px;
    background: radial-gradient(ellipse at center, var(--brand-green-soft) 0%, var(--brand-green) 75%);
  }
  .front-lockup {
    position: absolute; left: 0; right: 0; top: 130px;
    display: flex; align-items: center; justify-content: center; gap: 22px;
  }
  .brand-dot { width: 62px; height: 62px; border-radius: 50%; background: var(--paper); flex: none; }
  .brand-name {
    font-weight: 300; font-size: 82px; letter-spacing: 1px; line-height: 1; white-space: nowrap;
  }
  .card-front .brand-name { color: var(--paper); }
  .tagline {
    position: absolute; left: 0; right: 0; top: 262px; text-align: center;
    color: var(--paper); font-size: 15px; font-weight: 400; letter-spacing: 0.5px;
  }
  /* Back */
  .card-back { top: 470px; background: var(--paper); }
  .card-bands { position: absolute; inset: 0; }
  .back-lockup {
    position: absolute; left: 56px; top: 184px;
    display: flex; align-items: center; gap: 14px;
  }
  .card-back .brand-dot { width: 40px; height: 40px; background: var(--brand-green); }
  .card-back .brand-name { color: var(--logo-ink); font-size: 48px; letter-spacing: 0.5px; }
  .divider {
    position: absolute; left: 404px; top: 110px; width: 2px; height: 190px;
    background: var(--brand-green);
  }
  .contact { position: absolute; left: 430px; top: 100px; color: var(--ink); }
  .person-name { color: var(--brand-green); font-weight: 700; font-size: 19px; letter-spacing: 0.5px; }
  .person-title { font-size: 18px; font-weight: 400; margin-top: 2px; }
  .address { font-size: 13px; line-height: 1.35; margin-top: 18px; margin-left: 30px; }
  .contact-list { list-style: none; margin-top: 16px; margin-left: 38px; font-size: 13px; }
  .contact-list li { display: flex; align-items: center; gap: 10px; line-height: 1.6; }
  .contact-icon { width: 14px; height: 14px; flex: none; }
</style>
</head>
<body>
<main class="stage">
  <section class="card card-front" aria-label="Card front">
    <div class="world-map-area" role="img" aria-label="Faint dotted world map background"></div>
    <div class="front-lockup">
      <span class="brand-dot"></span>
      <span class="brand-name">kembrata</span>
    </div>
    <p class="tagline">Health technology sector selling into Health Plans</p>
  </section>

  <section class="card card-back" aria-label="Card back">
    <svg class="card-bands" viewBox="0 0 700 400" width="700" height="400" aria-hidden="true">
      <polygon points="0,0 700,0 700,14 220,14 205,58 0,58" fill="var(--brand-green)"/>
      <polygon points="222,22 700,22 700,30 218,30" fill="var(--brand-blue)"/>
      <polygon points="0,342 495,342 510,300 700,300 700,400 0,400" fill="var(--brand-green)"/>
      <polygon points="0,328 490,328 494,336 0,336" fill="var(--brand-blue)"/>
    </svg>
    <div class="back-lockup">
      <span class="brand-dot"></span>
      <span class="brand-name">kembrata</span>
    </div>
    <div class="divider"></div>
    <div class="contact">
      <p class="person-name">DARIN HOLLOWAY</p>
      <p class="person-title">Co-Founder</p>
      <p class="address">4810 N. Alder Road<br>Suite 2204 Ferndale.14</p>
      <ul class="contact-list">
        <li>
          <svg class="contact-icon" viewBox="0 0 16 16"><path d="M3 1l3 3-2 2c1 2 3 4 5 5l2-2 3 3-2 3C6 15 1 10 1 3z" fill="var(--brand-green)"/></svg>
          555-214-7390
        </li>
        <li>
          <svg class="contact-icon" viewBox="0 0 16 16"><rect x="1" y="3" width="14" height="10" fill="var(--brand-green)"/><path d="M1 3l7 6 7-6" fill="none" stroke="#fff" stroke-width="1.4"/></svg>
          info@kembrata.com
        </li>
        <li>
          <svg class="contact-icon" viewBox="0 0 16 16"><circle cx="8" cy="8" r="7" fill="var(--brand-green)"/><path d="M1 8h14M8 1c-3 4-3 10 0 14M8 1c3 4 3 10 0 14" fill="none" stroke="#fff" stroke-width="1"/></svg>
          www.kembrata.com
        </li>
      </ul>
    </div>
  </section>
</main>
</body>
</html>
```